July 2022 Industrial Manufacturer Product Expo Mexico City

We manufacture large screws and fastners for large Mining equipment, Trains, large ships, airplanes, wind turbines, and so on. We also do custom work base on the customer needs. No matter the size we can make it.
We have a Expo coming up with companies all over the world. We have to stand out we are a family own business so our customer service will be above and beyond anyone can provide. We do not have a sales force to push our products and services we provide one on one service.
Plus@!! I'm looking for anything that you designers can come up with if it was your company to put on a business card, plus i want to do a 1 or 2 sided pamphlet, and then a website. We make Speciality Bolts for large mining equipment these bolts can be 3 to 4 foot long!!! Plus fasteners, Nuts, washers, any, size, strengths, special materials, we offer more of a ono on one customer service, We are a small company, family own, but can fulfill any type of orders. We can also provide special time lines for emergency orders. "We keep the machines running we here at RWK don't believe in down time" We want to hear any slogan based on our company to stand out.
Thanks i really appreciate all your work and options that we have to pick on. Plus just a thought we could possibly want to entertain a experience Marketing internet help maybe a employment possibility. Thanks
Updates

I need 2 cards one in Spanish and English Like the steel back ground maybe send me in some bright red and blue writing Same with the Black cards Please remove the word Military The logo RWK maybe integrate a picture of a Bolt 🔩 Thank you

Still looking for I need 2 cards one in Spanish and English Like the steel back ground maybe send me in some bright red and blue writing Same with the Black cards try bright writing Please remove the word Military The logo RWK maybe integrate a picture of a Bolt 🔩 Plus will need the company to make a brochure and website next Thank you

Target Market(s)

Large Mining, Ship, Train, Green Energy, OPRE, and Government equipment. Throughout the World

Industry/Entity Type

We can Custom Manufacture any type of Fastners for Mining equipment, Trains, Ships, Green energy, Governments, or military projects. wind turbines,

Contact Information for Business Card

I attached the name and contact info that's on a card, plus the Company Logo. Would like industrial looking background with Bright Colors that will stand out!! If we can insert somewhere maybe on back that we "Custom Manufacture Any Size or Quantity Fastners for Large Mining Equipment, Trains, Ships, Green Energy Equipment or Government Projects

Font styles to use
Other font styles liked:
• You Pick, has to be bold, colorful standout, Professional looking Beable to read it.

Colors

Designer to choose colors to be used in the design.

Requirements
Must have
• Need in Spanish and English TO STANDOUT FROM THE REST OF THE EXPO!! See Business card details, Rounded corners
Nice to have
• Can i see some of the darker cards with Bright Red and Blue letters I like to see the different type of card material, heavy thickness, plastic, transparent, Metal types, Bright Colors, I saw like Raised letters like on the logo.

```html
<!DOCTYPE html>
<html lang="es">
<head>
<meta charset="utf-8">
<title>RWK – Tarjetas de presentación</title>
<link href="https://fonts.googleapis.com/css2?family=Source+Sans+3:wght@400;600&display=swap" rel="stylesheet">
<style>
  :root {
    --backdrop: #2a2a2a;
    --card: #000000;
    --blue: #0b8fd6;
    --red: #e3121a;
    --rule: #555555;
  }
  html, body {
    margin: 0;
    padding: 0;
    width: 1093px;
    height: 1200px;
    overflow: hidden;
    background: var(--backdrop);
    font-family: "Source Sans 3", "Myriad Pro", Arial, sans-serif;
  }
  .canvas {
    position: relative;
    width: 1093px;
    height: 1200px;
  }
  .card {
    position: absolute;
    left: 264px;
    width: 581px;
    height: 359px;
    background: var(--card);
    box-shadow: 3px 4px 6px rgba(0,0,0,0.6);
    text-align: center;
  }
  .card--front { top: 226px; }
  .card--back  { top: 620px; }

  .brand {
    position: absolute;
    left: 0;
    right: 0;
    display: flex;
    align-items: center;
    justify-content: center;
    gap: 14px;
  }
  .card--front .brand { top: 58px; }
  .card--back .brand  { top: 74px; }
  .brand__dot {
    width: 18px;
    height: 18px;
    border-radius: 50%;
    background: var(--blue);
  }
  .brand__name {
    font-size: 76px;
    line-height: 84px;
    font-weight: 600;
    letter-spacing: 6px;
    color: var(--blue);
  }

  .holder {
    position: absolute;
    top: 188px;
    left: 0;
    right: 0;
    margin: 0;
    font-size: 20px;
    font-weight: 600;
    color: var(--blue);
  }
  .rule {
    position: absolute;
    left: 253px;
    width: 75px;
    height: 1px;
    background: var(--rule);
    border: 0;
    margin: 0;
  }
  .rule--upper { top: 223px; }
  .rule--lower { top: 284px; }
  .quotes {
    position: absolute;
    top: 230px;
    left: 0;
    right: 0;
    margin: 0;
    font-size: 16px;
    line-height: 22px;
    color: var(--red);
  }
  .phones {
    position: absolute;
    top: 294px;
    left: 0;
    right: 0;
    display: flex;
    justify-content: center;
    align-items: center;
    gap: 4px;
    font-size: 16px;
    color: var(--red);
  }
  .phones__icon { width: 16px; height: 16px; }
  .phones__item { display: flex; align-items: center; gap: 5px; }
  .phones__item + .phones__item { margin-left: 6px; }

  .tagline {
    position: absolute;
    top: 229px;
    left: 0;
    right: 0;
    margin: 0;
    font-size: 18.5px;
    line-height: 23.5px;
    color: var(--red);
  }
</style>
</head>
<body>
<main class="canvas">
  <section class="card card--front" aria-label="Frente de la tarjeta">
    <div class="brand">
      <span class="brand__dot"></span>
      <span class="brand__name">RWK</span>
    </div>
    <h1 class="holder">Lic. Mariana Estela Ruiz Campos</h1>
    <hr class="rule rule--upper">
    <p class="quotes">Cotizaciones en<br>tornilleriarwk.ventas@example.com</p>
    <hr class="rule rule--lower">
    <div class="phones">
      <span class="phones__item">
        <svg class="phones__icon" viewBox="0 0 24 24" aria-hidden="true">
          <path fill="#0b8fd6" d="M6.6 10.8a15.1 15.1 0 0 0 6.6 6.6l2.2-2.2a1 1 0 0 1 1-.25 11.4 11.4 0 0 0 3.6.57 1 1 0 0 1 1 1V20a1 1 0 0 1-1 1A17 17 0 0 1 3 4a1 1 0 0 1 1-1h3.5a1 1 0 0 1 1 1c0 1.25.2 2.45.57 3.57a1 1 0 0 1-.25 1z"/>
          <path fill="none" stroke="#0b8fd6" stroke-width="1.8" d="M14 3.5a7 7 0 0 1 6.5 6.5M14 7a3.5 3.5 0 0 1 3 3"/>
        </svg>
        5550142877
      </span>
      <span class="phones__item">
        <svg class="phones__icon" viewBox="0 0 24 24" aria-hidden="true">
          <rect x="6" y="2" width="12" height="20" rx="2" fill="none" stroke="#0b8fd6" stroke-width="2"/>
          <circle cx="12" cy="18.5" r="1.2" fill="#0b8fd6"/>
        </svg>
        5550193462
      </span>
    </div>
  </section>

  <section class="card card--back" aria-label="Reverso de la tarjeta">
    <div class="brand">
      <span class="brand__dot"></span>
      <span class="brand__name">RWK</span>
    </div>
    <p class="tagline" lang="en">Custom Manufacture Any Size or<br>Quantity Fastners for Large&nbsp; Mining<br>Equipment Trains, Ships, Green Energy<br>Equipment or Government Projects</p>
  </section>
</main>
</body>
</html>
```